ZiPU Vortal Bhutan Trip

This is a one-page (A5) flyer to attract sign ups for Bhutan Trip.

Target Market(s)

Young entrepreneurs (worldwide)

Requirements
Must have
• Must have "WOW" effect and attract sign ups
Nice to have
• Striking and vibrant

```html
<!DOCTYPE html>
<html lang="en">
<head>
<meta charset="utf-8">
<title>ZiPU Vortal Bhutan Trip</title>
<link href="https://fonts.googleapis.com/css2?family=Oswald:wght@400;500;600;700&family=Open+Sans:wght@400;600;700;800&family=Kaushan+Script&display=swap" rel="stylesheet">
<style>
:root{
  --navy:#13306b;
  --orange:#f39a1e;
  --orange-deep:#e0701a;
  --red:#d62a24;
  --green:#4fa82c;
  --green-deep:#3a8a1f;
  --yellow:#ffd21f;
  --white:#ffffff;
  --paper:#f1f2f4;
  --ink:#1d2f5c;
  --sky-top:#2c3440;
  --sky-mid:#8a7a6a;
  --roof:#6c2c22;
}
*{margin:0;padding:0;box-sizing:border-box}
html,body{width:849px;height:1200px;overflow:hidden;background:var(--white)}
body{font-family:"Open Sans",Arial,sans-serif;color:var(--ink)}
.flyer{position:relative;width:849px;height:1200px;overflow:hidden;background:var(--paper)}
.hero-photo{position:absolute;left:0;top:0;width:849px;height:540px;
  background:linear-gradient(180deg,var(--sky-top) 0%,#4b4a4c 30%,var(--sky-mid) 55%,var(--roof) 78%,#c9b89c 100%)}
.title{position:absolute;top:14px;left:0;width:100%;text-align:center;white-space:nowrap}
.title .brand{font-family:"Open Sans",sans-serif;font-weight:800;color:var(--white);font-size:40px;vertical-align:middle}
.title .trip{font-family:"Kaushan Script",cursive;color:var(--yellow);font-size:56px;vertical-align:middle;margin-left:10px}
.ribbon{position:absolute;top:0;right:0;width:150px;height:150px;overflow:hidden}
.ribbon span{position:absolute;top:38px;right:-46px;width:210px;transform:rotate(45deg);background:var(--red);
  color:var(--white);font-family:"Oswald",sans-serif;font-weight:600;font-size:15px;line-height:1.05;text-align:center;padding:6px 0}
.headline{position:absolute;top:102px;left:0;width:100%;text-align:center;font-family:"Oswald",sans-serif;
  font-weight:700;color:var(--white);text-transform:uppercase;text-shadow:0 2px 6px rgba(0,0,0,.5)}
.headline .l1{font-size:32px;font-weight:600;display:block}
.headline .l2,.headline .l3{font-size:48px;line-height:1.1;display:block}
.headline .hi{color:var(--orange)}
.panel{position:absolute;left:0;top:0;width:849px;height:1200px}
.date{position:absolute;left:339px;top:432px;width:200px;text-align:center;font-family:"Oswald",sans-serif;color:var(--navy);font-weight:700}
.date .days,.date .year{font-size:42px;line-height:1}
.date svg{display:block;margin:0 auto 4px}
.benefits{position:absolute;left:40px;top:558px;list-style:none;width:520px}
.benefits li{font-family:"Oswald",sans-serif;font-size:23px;color:var(--navy);line-height:40px;white-space:nowrap;display:flex;align-items:center}
.benefits li svg{margin-right:12px;flex:none}
.benefits b{color:var(--orange);font-weight:700;margin-right:8px}
.snap{position:absolute;border:6px solid var(--white);box-shadow:0 4px 10px rgba(0,0,0,.3)}
.snap.crowd{left:585px;top:495px;width:240px;height:175px;transform:rotate(3deg);background:linear-gradient(160deg,#6a5b52,#b9413a 50%,#d89a5a)}
.snap.valley{left:580px;top:690px;width:245px;height:165px;transform:rotate(-4deg);background:linear-gradient(180deg,#9ab9d6,#5f8a52 55%,#355a2a)}
.snap.fort{left:605px;top:878px;width:225px;height:150px;transform:rotate(2deg);background:linear-gradient(180deg,#3f70c0,#8fb3e0 45%,#e8e2d6 65%,#496b3a)}
.price{position:absolute;left:57px;top:860px;width:170px;height:170px;border-radius:50%;background:var(--navy);border:5px solid var(--white);
  box-shadow:0 3px 8px rgba(0,0,0,.3);color:var(--white);text-align:center;font-family:"Oswald",sans-serif;padding-top:42px}
.price .lbl{font-size:24px;display:block;line-height:1}
.price .amt{font-size:38px;font-weight:700;display:block;line-height:1.15}
.early{position:absolute;left:272px;top:880px;font-family:"Oswald",sans-serif;color:var(--navy);white-space:nowrap}
.early .lbl{font-size:25px;display:block;line-height:1.2;color:#2a78c8}
.early .amt{font-size:30px;font-weight:700;color:var(--navy)}
.early .note{font-size:16px}
.cta{position:absolute;left:0;top:1048px;width:849px;height:64px;background:linear-gradient(180deg,var(--green),var(--green-deep));
  display:flex;align-items:center;padding:0 24px;color:var(--white)}
.cta .go{font-family:"Oswald",sans-serif;font-weight:700;font-size:38px;margin-right:14px}
.cta .limit{font-family:"Oswald",sans-serif;font-size:28px;font-weight:500}
.cta .contact{margin-left:auto;font-family:"Open Sans",sans-serif;font-weight:700;font-size:19px;line-height:1.15}
.footer{position:absolute;left:0;top:1112px;width:849px;height:88px;background:var(--white);display:flex;align-items:center;padding:0 24px}
.footer .by{font-size:13px;font-weight:700;color:var(--ink);width:135px;line-height:1.25}
.footer .host{font-family:"Open Sans",sans-serif;font-weight:800;color:var(--orange);font-size:26px;display:flex;align-items:center;gap:8px}
.footer .host i{display:inline-block;width:16px;height:16px;border-radius:50%;background:var(--orange)}
.footer .support{margin-left:auto;display:flex;align-items:center;gap:18px}
.footer .support .by{width:auto}
.badge{width:60px;height:40px;border-radius:6px;background:#d8dde4}
.badge.round{width:46px;height:46px;border-radius:50%;background:#cfe3c4}
.badge.wide{width:80px;background:#f2dcb8}
</style>
</head>
<body>
<div class="flyer">
  <div class="hero-photo" role="img" aria-label="Traditional Bhutanese dzong fortress with ornate wooden facade and courtyard under a dusky sky"></div>

  <svg class="panel" width="849" height="1200" viewBox="0 0 849 1200" aria-hidden="true">
    <defs>
      <linearGradient id="paperFill" x1="0" y1="0" x2="0" y2="1">
        <stop offset="0" stop-color="#ffffff"/>
        <stop offset="1" stop-color="#e6e8ec"/>
      </linearGradient>
    </defs>
    <path d="M0 490 L849 420 L849 1200 L0 1200 Z" fill="url(#paperFill)"/>
    <path d="M0 482 L849 412 L849 422 L0 492 Z" fill="#f39a1e"/>
  </svg>

  <h1 class="title"><span class="brand">ZiPU Vortal</span><span class="trip">Bhutan Trip</span></h1>
  <div class="ribbon"><span>HURRY<br>LIMITED SLOTS</span></div>

  <h2 class="headline">
    <span class="l1">Sign up for a once</span>
    <span class="l2">In a lifetime <span class="hi">experience</span></span>
    <span class="l3">In the land of happiness!</span>
  </h2>

  <div class="date">
    <svg width="28" height="28" viewBox="0 0 24 24"><path d="M12 1l3.2 7 7.6.8-5.7 5.1 1.7 7.5L12 17.6 5.2 21.4l1.7-7.5L1.2 8.8 8.8 8z" fill="#f39a1e"/></svg>
    <div class="days">3-6 JULY</div>
    <div class="year">2017</div>
  </div>

  <ul class="benefits">
    <li><svg width="22" height="20" viewBox="0 0 24 22"><path d="M2 12l7 7L22 3" fill="none" stroke="#f39a1e" stroke-width="4"/></svg><b>LEARN</b>FROM LEADING SOCIAL CHANGE MAKERS</li>
    <li><svg width="22" height="20" viewBox="0 0 24 22"><path d="M2 12l7 7L22 3" fill="none" stroke="#f39a1e" stroke-width="4"/></svg><b>ENGAGE</b>THE COMMUNITY THROUGH VOLUNTEERING</li>
    <li><svg width="22" height="20" viewBox="0 0 24 22"><path d="M2 12l7 7L22 3" fill="none" stroke="#f39a1e" stroke-width="4"/></svg><b>DISCOVER</b>YOUR INNER HAPPINESS</li>
    <li><svg width="22" height="20" viewBox="0 0 24 22"><path d="M2 12l7 7L22 3" fill="none" stroke="#f39a1e" stroke-width="4"/></svg><b>SAVOUR</b>SAVOUR ORGANIC FOOD</li>
    <li><svg width="22" height="20" viewBox="0 0 24 22"><path d="M2 12l7 7L22 3" fill="none" stroke="#f39a1e" stroke-width="4"/></svg><b>IMMERSE</b>IN TRADITIONAL SPORTS AND CRAFT</li>
    <li><svg width="22" height="20" viewBox="0 0 24 22"><path d="M2 12l7 7L22 3" fill="none" stroke="#f39a1e" stroke-width="4"/></svg><b>EXPERIENCE</b>WARM BHUTANESE HOSPITALITY</li>
    <li><svg width="22" height="20" viewBox="0 0 24 22"><path d="M2 12l7 7L22 3" fill="none" stroke="#f39a1e" stroke-width="4"/></svg><b>REJUVENATE</b>YOUR MIND, BODY AND SOUL</li>
  </ul>

  <div class="snap crowd" role="img" aria-label="Crowd gathered at a colourful Bhutanese festival"></div>
  <div class="snap valley" role="img" aria-label="Green Himalayan valley with terraced fields"></div>
  <div class="snap fort" role="img" aria-label="White dzong fortress under a blue sky"></div>

  <div class="price"><span class="lbl">Price at</span><span class="amt">USD 2800</span></div>
  <div class="early">
    <span class="lbl">Early bird discount</span>
    <span class="amt">USD2300</span> <span class="note">(If you sign up by 31 March 2017)</span>
  </div>

  <div class="cta">
    <span class="go">Register now!</span>
    <span class="limit">Limited to 30 participants!</span>
    <span class="contact">Email:<br>hello@trailfound.sg</span>
  </div>

  <footer class="footer">
    <span class="by">Exclusively Brought<br>To You By:</span>
    <span class="host"><i></i>ZiPU Vortal</span>
    <div class="support">
      <span class="by">Supported By:</span>
      <span class="badge"></span>
      <span class="badge round"></span>
      <span class="badge wide"></span>
    </div>
  </footer>
</div>
</body>
</html>
```